Retractable Banner Design Featuring Key Product for Beauty Trade Show

We're a beauty/nail supply company that specializes in products used in professional nail salons. The key product for this design is Disposable Latex Gloves.
We will be exhibiting in a trade show this summer and are looking for a free-standing Retractable Banner Design that will be displayed at the front of our booth. The goal of the banner will be to display key products that are high in demand with our customers. The banner will be used to attract attention and highlight key selling points of these popular products. We would like the banner to be focused on the product title, image and key points, with a beauty/model/pattern background to create a professional appearance.
Nail Salons
Nail & Beauty Industry

```html
<!DOCTYPE html>
<html lang="en">
<head>
<meta charset="utf-8">
<title>Latex Gloves Retractable Banner</title>
<link rel="stylesheet" href="https://fonts.googleapis.com/css2?family=Montserrat:wght@500;700;800&display=swap">
<style>
  :root{
    --ink:#1b1b1b;
    --orange-deep:#d35400;
    --orange-mid:#e06a00;
    --orange-warm:#ee8f00;
    --title-orange:#d9590a;
    --white:#ffffff;
    --page:#ffffff;
  }
  *{margin:0;padding:0;box-sizing:border-box}
  html,body{width:1200px;height:1200px;overflow:hidden;background:var(--page)}
  .stage{position:relative;width:1200px;height:1200px}
  .banner{position:absolute;left:376px;top:40px;width:448px;height:1120px;overflow:hidden}
  .banner-inner{position:absolute;left:0;top:0;width:664px;height:1660px;transform:scale(0.6747);transform-origin:0 0;font-family:"Montserrat",sans-serif;color:var(--white)}
  .backdrop{position:absolute;inset:0;width:664px;height:1660px}
  .title{position:absolute;left:68px;top:50px;font-size:64px;font-weight:800;color:var(--title-orange);letter-spacing:-0.5px;white-space:nowrap}
  .pack-icon{position:absolute;left:86px;top:148px;width:82px;height:82px}
  .pack-info{position:absolute;left:192px;top:146px;font-size:33px;font-weight:500;line-height:53px;white-space:nowrap}
  .salon-photo{position:absolute;left:302px;top:250px;width:372px;height:372px;border-radius:50%;border:6px solid var(--white);background:radial-gradient(circle at 45% 40%,#f3e9e3 0%,#c9b2a6 45%,#5b514d 80%,#2a2a2a 100%)}
  .product-photo{position:absolute;left:0;top:474px;width:550px;height:500px;background:linear-gradient(160deg,#f2ede8 0%,#f1ece6 38%,#e8702a 60%,#d75a12 100%);border-radius:6px 40px 6px 6px}
  .features{position:absolute;left:78px;top:1058px;list-style:none}
  .feature{position:relative;padding-left:38px;margin-bottom:52px;white-space:nowrap}
  .feature::before{content:"";position:absolute;left:0;top:0;width:4px;height:90px;background:var(--white)}
  .feature-lead{display:block;font-size:34px;font-weight:500;line-height:42px}
  .feature-key{display:block;font-size:39px;font-weight:800;line-height:54px}
</style>
</head>
<body>
<div class="stage">
  <section class="banner">
    <div class="banner-inner">
      <svg class="backdrop" viewBox="0 0 664 1660" aria-hidden="true">
        <defs>
          <linearGradient id="orangeFade" x1="0" y1="0" x2="0" y2="1">
            <stop offset="0" stop-color="#d35400"/>
            <stop offset="0.6" stop-color="#e06a00"/>
            <stop offset="1" stop-color="#ee8f00"/>
          </linearGradient>
        </defs>
        <rect width="664" height="1660" fill="var(--ink)"/>
        <path d="M0,245 C260,320 520,520 664,780 L664,1660 L0,1660 Z" fill="url(#orangeFade)"/>
        <path d="M0,335 C290,420 560,660 664,920 L664,1090 C560,780 300,520 0,465 Z" fill="var(--ink)"/>
        <path d="M0,770 C200,820 380,900 470,980 C360,930 180,900 0,900 Z" fill="var(--ink)"/>
      </svg>

      <h1 class="title">LATEX GLOVES</h1>

      <svg class="pack-icon" viewBox="0 0 82 82" fill="none" stroke="#fff" stroke-width="3" stroke-linejoin="round" stroke-linecap="round" aria-hidden="true">
        <path d="M10,78 L10,46 L6,30 L8,12 L13,12 L14,28 L16,6 L21,6 L21,28 L24,4 L29,4 L28,28 L32,8 L37,9 L34,34 L42,30 L44,35 L34,50 L34,78 Z"/>
        <path d="M40,78 L40,58 L46,40 L50,18 L55,18 L55,36 L60,14 L65,15 L61,38 L68,20 L73,22 L67,42 L75,34 L79,38 L66,60 L58,72 L56,78"/>
      </svg>
      <p class="pack-info">1,000 Pcs/Case<br>84 Cases Per Pallet</p>

      <div class="salon-photo" role="img" aria-label="Photo of a nail technician in latex gloves shaping a client's nails"></div>
      <div class="product-photo" role="img" aria-label="Photo of a case of textured latex gloves with gloved hands reaching out"></div>

      <ul class="features">
        <li class="feature"><span class="feature-lead">100% Powder-Free</span><span class="feature-key">No residue or irritants</span></li>
        <li class="feature"><span class="feature-lead">Premium Textured Grip</span><span class="feature-key">For Superior Grip</span></li>
        <li class="feature"><span class="feature-lead">6.2g Latex</span><span class="feature-key">Super Heavy Duty</span></li>
        <li class="feature"><span class="feature-lead">Designed for</span><span class="feature-key">Professional Salons!</span></li>
      </ul>
    </div>
  </section>
</div>
</body>
</html>
```